Savour and Thrive Wellbeing is being Launched and needs a business card and stationery package

I need a stationery package including business card (primary focus) , letterhead, digital letterhead, envelopes, with compliments slip, A 5 note sheet for the rebranding of my business and launch of my new website. I have a logo, like beige, brown earthy tones with a hint of red. I would also like the option of my letterhead also being printed on recycled paper in another format as well as the traditional letterhead. I do also send my letters to GPs and specialists digitally as well. I like to stand out from the usual stereotype of fruits and vegetables on business cards as I find that quite tacky and stereotypical. I want the business card to capture the essence of my logo as natural, nutrition, enjoyment, nurturing and freedom with food. I have attached the logo, and additional brief sheet on my ideas. Happy to have any background that is complementary to my theme, and what you believe would be catching. Definitely DONT'T like pink, try to pick up the darker colour in the logo please. and think too much black is a little overpowering.

Target Market(s)

clients who are interested in improving their health and wellness. Client 80% females; 20% males

Industry/Entity Type

Health And Wellness

Contact Information for Business Card

I am open to having different backgrounds as well that would complement the logo. Probably less emphasis on the heart out of the logo - just happy to keep that in the logo only please
I am also wanting two business cards - one for the appointments, one for general distribution and media distribution (both need to look consistent though) - but does give opportunity for one of the business cards to be less wordy and more striking. And the front of the business card can certainly stand out with the entire savour and thrive logo and my name and grab the attention of the receiver.
1st business card
on front:
Lorena Whitcombe
Savour and Thrive Wellbeing & logo
Nutritionist and Dietitian
Tarvel Medical Centre
647 Brindle Hill Rd, Quorrel Q 4987
Phone: (07) 3017 2968 Fax: (07) 3156 7209
Mobile: 0400 261 937
www.savourandthrivewellbeing.example.au
lorena@savourandthrivewellbeing.example.au
on back:
next appointment

……………………….. at ……………………… (possibly 4 times)
If you are unable to keep your appointment, please contact us as soon as possible (small font)
2nd business card (needs to be very eye catching and stand out)
on front: Savour and Thrive Wellbeing logo and my name
on back:
Lorena Whitcombe
address
phones, fax, website, email address

Font styles to use
Other font styles liked:
• please refer to logo

Requirements
Must have
• refreshing and simple; new and vibrant - I am rebranding my business after 20 years
• to get a feel of what is the theme - go to my new website (not completed as yet - but you will get a preliminary view) - don't do as google search as blocked - but can put into website header and it will be shown
• www.savourandthrivewellbeing.example.au - but please ignore the colouring of the 4 blocks under the slider on the home page - I am not wanting these colourings - they are getting updated.
Nice to have
• earthy tones, beige, hint of red, fonts to match logo if possible, organic, modern
• get inspiration from my logo please, open to having other backgrounds that complement
Should not have
• no food shots or stereotypical weight/ scales images
• no green, yellow or orange

```html
<!DOCTYPE html>
<html lang="en">
<head>
<meta charset="utf-8">
<title>Savour and Thrive Wellbeing – Business Cards</title>
<link rel="stylesheet" href="https://fonts.googleapis.com/css2?family=Courgette&family=Didact+Gothic&family=PT+Sans:ital,wght@0,700;1,400&display=swap">
<style>
  :root {
    --backdrop: #d8d2cb;
    --card-dark: #2f2a30;
    --card-light: #efeeeb;
    --berry: #a8344f;
    --berry-soft: #b8546c;
    --ink-light: #f4f1ee;
    --ink-dark: #3a3637;
    --ink-muted: #5b5657;
    --rule-dots: #8c8788;
  }
  * { box-sizing: border-box; margin: 0; padding: 0; }
  html, body {
    width: 1200px; height: 987px; overflow: hidden;
    background: var(--backdrop);
  }
  .card {
    position: absolute; left: 292px; width: 616px; height: 349px;
    box-shadow: 0 4px 14px rgba(0,0,0,.25);
  }
  .card--front { top: 131px; background: var(--card-dark); color: var(--ink-light); font-family: "Didact Gothic", sans-serif; }
  .card--appointment { top: 506px; background: var(--card-light); color: var(--ink-dark); font-family: "PT Sans", sans-serif; }

  .brand {
    position: absolute; left: 0; right: 0; top: 62px;
    display: flex; flex-direction: column; align-items: center; gap: 12px;
  }
  .brand__dot { width: 34px; height: 34px; border-radius: 50%; background: var(--berry-soft); }
  .brand__name { font-size: 24px; color: var(--berry-soft); letter-spacing: .5px; }

  .title-line {
    position: absolute; left: 37px; right: 34px; top: 192px;
    display: flex; align-items: center; gap: 6px; white-space: nowrap;
  }
  .title-line__rule { flex: 1; height: 1px; background: var(--ink-light); }
  .title-line__name { font-family: "Courgette", cursive; font-size: 19px; color: var(--berry); }
  .title-line__role { font-size: 16px; }
  .title-line__dash { color: var(--berry); font-size: 17px; }

  .contact { position: absolute; top: 235px; font-size: 16px; line-height: 23.5px; }
  .contact--left { left: 35px; }
  .contact--right { right: 34px; text-align: right; }
  .contact__label { color: var(--berry); }
  .contact__small { font-size: 14px; }

  .appointment__heading {
    position: absolute; left: 37px; top: 57px;
    font-size: 19px; font-weight: 700; color: var(--berry); letter-spacing: .2px;
  }
  .appointment__brand {
    position: absolute; right: 34px; top: 28px; width: 170px;
    display: flex; flex-direction: column; align-items: center; gap: 8px; text-align: center;
  }
  .appointment__brand .brand__dot { width: 22px; height: 22px; background: var(--berry); }
  .appointment__brand-name { font-size: 17px; font-weight: 700; line-height: 20px; color: var(--ink-dark); }

  .slots { position: absolute; left: 35px; right: 34px; top: 84px; list-style: none; }
  .slot { display: flex; align-items: flex-end; height: 49px; font-size: 13px; color: var(--ink-muted); }
  .slot__blank { border-bottom: 1px dotted var(--rule-dots); height: 14px; }
  .slot__blank--date { width: 276px; }
  .slot__blank--time { flex: 1; }
  .slot__at { padding: 0 6px; line-height: 14px; }

  .appointment__note {
    position: absolute; left: 0; right: 0; top: 304px; text-align: center;
    font-size: 13px; font-style: italic; color: var(--ink-muted);
  }
</style>
</head>
<body>
  <section class="card card--front">
    <div class="brand">
      <span class="brand__dot"></span>
      <span class="brand__name">Savour and Thrive Wellbeing</span>
    </div>
    <div class="title-line">
      <span class="title-line__rule"></span>
      <span class="title-line__name">Lorena Whitcombe</span>
      <span class="title-line__dash">-</span>
      <span class="title-line__role">Nutritionist and Dietitian</span>
      <span class="title-line__rule"></span>
    </div>
    <div class="contact contact--left">
      <div><span class="contact__label">Tel.</span> (07) 3017 2968</div>
      <div><span class="contact__label">Fax.</span> (07) 3156 7209</div>
      <div><span class="contact__label">Mob.</span> 0400 261 937</div>
      <div class="contact__small">lorena@savourandthrivewellbeing.example.au</div>
    </div>
    <div class="contact contact--right">
      <div>Tarvel Medical Centre</div>
      <div>647 Brindle Hill Rd</div>
      <div>Quorrel Q 4987</div>
      <div class="contact__small">savourandthrivewellbeing.example.au</div>
    </div>
  </section>

  <section class="card card--appointment">
    <h2 class="appointment__heading">NEXT APPOINTMENT</h2>
    <div class="appointment__brand">
      <span class="brand__dot"></span>
      <span class="appointment__brand-name">Savour and Thrive Wellbeing</span>
    </div>
    <ul class="slots">
      <li class="slot"><span class="slot__blank slot__blank--date"></span><span class="slot__at">at</span><span class="slot__blank slot__blank--time"></span></li>
      <li class="slot"><span class="slot__blank slot__blank--date"></span><span class="slot__at">at</span><span class="slot__blank slot__blank--time"></span></li>
      <li class="slot"><span class="slot__blank slot__blank--date"></span><span class="slot__at">at</span><span class="slot__blank slot__blank--time"></span></li>
      <li class="slot"><span class="slot__blank slot__blank--date"></span><span class="slot__at">at</span><span class="slot__blank slot__blank--time"></span></li>
    </ul>
    <p class="appointment__note">If you are unable to keep your appointment, please contact us as soon as possible</p>
  </section>
</body>
</html>
```